Bold Modern Creative Wine Label Needed for a Chardonnay

We need a modern, eye catching label, one that will appeal to millennials, but also attract the older more conservative crowd. We like the boldness of black on white but are open to your suggestions. Since the bottle type is a light green 'burgundy style' bottle, you should take that into account. The name of the brand is Vo`. The attached label is example of what we like very much. It is eye catching and bold and modern. Keep in mind that the bottle will be light green in color so black and white might not work so well. Use your creativity please! The label can be any size but needs to fit on this shape bottle. See attached photos. thanks!!

(Please no grapes or wine glasses or wine bottles featured on the label!)
Updates

Hi Designers, I just wanted to let you know that we received many great designs and we are sorting through them this week. The website is making it a bit difficult to create a 'poll' so this is taking longer than we expected. Thanks for all the great submissions!

```html
<!DOCTYPE html>
<html lang="en">
<head>
<meta charset="utf-8">
<title>Vo` Chardonnay 2019 – Label</title>
<link rel="stylesheet" href="https://fonts.googleapis.com/css2?family=Cormorant+Garamond:wght@500&display=swap">
<style>
  :root {
    --paper: #ffffff;
    --ink: #0a0a0a;
    --rule: #2a2a2a;
  }
  html, body {
    margin: 0;
    padding: 0;
    width: 1200px;
    height: 772px;
    overflow: hidden;
    background: var(--paper);
  }
  .canvas {
    position: relative;
    width: 1200px;
    height: 772px;
    background: var(--paper);
    color: var(--ink);
    font-family: "Cormorant Garamond", "Times New Roman", serif;
    font-weight: 500;
    font-variant-numeric: lining-nums;
  }
  .brand-name {
    position: absolute;
    left: 0;
    right: 0;
    top: 215px;
    margin: 0;
    text-align: center;
    font-size: 120px;
    font-weight: 500;
    line-height: 1;
    white-space: nowrap;
  }
  .varietal {
    position: absolute;
    left: 50%;
    top: 502px;
    width: 294px;
    transform: translateX(-50%);
    text-align: center;
    font-size: 22px;
    line-height: 22px;
  }
  .varietal::before {
    content: "";
    position: absolute;
    left: 0;
    right: 0;
    top: 12px;
    border-top: 1px solid var(--rule);
  }
  .vintage {
    position: absolute;
    left: 0;
    right: 0;
    top: 538px;
    text-align: center;
    font-size: 25px;
    line-height: 1;
  }
</style>
</head>
<body>
  <main class="canvas">
    <h1 class="brand-name">Vo`</h1>
    <div class="varietal">chardonnay</div>
    <div class="vintage">2019</div>
  </main>
</body>
</html>
```